Vehcile and Personal GPS Tracking Service Needs Brochure

We need a brochure design for our serviced called Harbor Beacon Locate (HBL) www.harborbeaconlocate.com (info site) & www.harborbeaconlocate.net (our actually gps tracking site).

HBL provides a Live GPS Tracking service for vehicles and personal trackers (key tag size).

We need a brochure that will describe our products and its benefits.

The use of our product allows corporate companies to track their vehcile fleets and security their goods and vehciles.

Security is a big issues in our country. Car theif is common. Also, kidnapping of CEOs is a concern.

Our target audience are corporate companys, who are interested in managing their vehcile fleets and ensuring the security of their vehicles and staff memebers.

We would like to continue using the corporate colours of yellow and grey.

The design should communicate reliablity and safety.

Target Market(s)

Medium to large companies (10 or more vehciles). CEOs.

Industry/Entity Type

Security

Requirements
Must have
• Plese see the attached word document that we are providing customers.
Nice to have
• It would be good to have a picture of a vehcile being tracking on a map, so people have a visual of how it works.
Should not have
• The brouchure should not include pricing, as this may change. However, we would like to show that we hae to different rates for self montioring and security monitoring.

```html
<!DOCTYPE html>
<html lang="en">
<head>
<meta charset="utf-8">
<title>Harbor Beacon Locate – Brochure</title>
<link rel="stylesheet" href="https://fonts.googleapis.com/css2?family=Questrial&family=Montserrat:wght@600;700&display=swap">
<style>
:root{
  --yellow:#f5c400;
  --cover-grey:#77787b;
  --cover-grey-dark:#66676a;
  --bar-grey:#8c8c8e;
  --box-grey:#e6e6e7;
  --ink:#3c3c3e;
  --text:#6a6a6c;
  --paper:#ffffff;
  --stage:#4b3a2d;
}
*{box-sizing:border-box;margin:0;padding:0}
html,body{width:1200px;height:900px;overflow:hidden;background:var(--stage)}
body{position:relative;font-family:"Questrial",sans-serif;color:var(--text)}
.page{position:absolute;width:285px;height:410px;background:var(--paper);overflow:hidden;box-shadow:0 2px 6px rgba(0,0,0,.35)}
.row-top{top:22px}.row-bottom{top:452px}
.col-1{left:14px}.col-2{left:310px}.col-3{left:611px}.col-4{left:904px}
.page--cover{background:linear-gradient(180deg,var(--cover-grey),var(--cover-grey-dark))}
.swoosh{position:absolute;left:0;bottom:0;width:100%;height:130px}
.heading{position:absolute;font-family:"Questrial",sans-serif;color:var(--yellow);font-size:15px}
.subhead{position:absolute;font-family:"Montserrat",sans-serif;font-weight:600;color:var(--ink);font-size:7px}
.body-text{position:absolute;font-size:5px;line-height:1.45;color:var(--text)}
.bar{position:absolute;height:9px;background:var(--bar-grey);color:#fff;font-size:5px;text-align:center;line-height:9px;text-transform:uppercase}
.feature-box{position:absolute;background:var(--box-grey);border-radius:3px;padding:3px 4px;font-size:4px;line-height:1.4}
.feature-box b{display:block;color:#c89d00;font-family:"Montserrat",sans-serif;font-size:4.2px;margin-bottom:1px}
.placeholder{position:absolute;border-radius:2px}
.tick-list{position:absolute;display:grid;grid-template-columns:1fr 1fr;gap:9px 10px}
.tick-item{display:flex;gap:5px;align-items:flex-start;font-size:4.3px;line-height:1.4}
.tick{flex:0 0 11px;width:11px;height:11px}
.brand-name{font-family:"Questrial",sans-serif;letter-spacing:.5px}
</style>
</head>
<body>

<!-- Back cover -->
<section class="page page--cover row-top col-1">
  <svg class="swoosh" style="height:230px" viewBox="0 0 285 230" preserveAspectRatio="none" aria-hidden="true">
    <path d="M0 60 Q140 0 285 40 L285 230 L0 230Z" fill="#ffffff" opacity=".06"/>
    <path d="M0 140 Q150 70 285 110 L285 230 L0 230Z" fill="#ffffff" opacity=".06"/>
  </svg>
  <p class="body-text" style="left:60px;top:272px;width:165px;text-align:center;color:#fff">For further information on our services or a live demonstration on how our website works, please contact us:</p>
  <p class="body-text" style="left:0;top:318px;width:285px;text-align:center;color:var(--yellow);font-size:6px">Dana Merrow</p>
  <p class="body-text" style="left:0;top:326px;width:285px;text-align:center;color:#fff;font-size:6px">Director</p>
  <p class="body-text" style="left:0;top:343px;width:285px;text-align:center;color:#fff;font-size:5.5px"><span style="color:var(--yellow)">Email:</span> dana@harborbeaconlocate.com &nbsp; <span style="color:var(--yellow)">Ph:</span> 555 0142</p>
</section>

<!-- Front cover -->
<section class="page page--cover row-top col-2">
  <svg class="swoosh" style="height:200px" viewBox="0 0 288 200" preserveAspectRatio="none" aria-hidden="true">
    <path d="M0 70 Q150 10 288 60 L288 200 L0 200Z" fill="#ffffff" opacity=".07"/>
    <path d="M0 150 Q140 90 288 130 L288 200 L0 200Z" fill="#ffffff" opacity=".07"/>
  </svg>
  <svg style="position:absolute;left:100px;top:68px" width="88" height="88" aria-hidden="true"><circle cx="44" cy="44" r="44" fill="#e9e9ea"/></svg>
  <p class="brand-name" style="position:absolute;left:0;top:170px;width:288px;text-align:center;color:#fff;font-size:19px;line-height:1.15">HARBOR BEACON<br>LOCATE</p>
</section>

<!-- Welcome -->
<section class="page row-top col-3">
  <svg style="position:absolute;left:120px;top:24px" width="14" height="14" aria-hidden="true"><circle cx="7" cy="7" r="7" fill="#9a9a9c"/></svg>
  <p class="brand-name" style="position:absolute;left:0;top:42px;width:285px;text-align:center;font-size:7px;color:var(--ink)">HARBOR BEACON LOCATE</p>
  <h1 class="heading" style="left:0;top:100px;width:285px;text-align:center">Welcome</h1>
  <div class="body-text" style="left:22px;top:124px;width:242px">
    <p>Welcome to Harbor Beacon Locate services. Our website offers real time live GPS tracking services.</p><br>
    <p>Using GPS satellite technology, Harbor Beacon Locate's service enables you to see a vehicle or person move on a computer screen in real time. This enables you to know precisely where the car or person is. Our car tracking service can be used to track any type of vehicle or a fleet of vehicles. Our hand held personal trackers can be carried by anyone.</p><br>
    <p>The tracking system can be accessed at any time from a computer in the privacy of your own office or home or on an internet mobile device (tablet or smart phone), enabling you to see a car's or person's path in real time. You do not need to purchase or install any special software on your computer – our service enables you to track a vehicle or person live from anywhere you have internet connection.</p>
  </div>
  <div class="placeholder" role="img" aria-label="Security camera product photo" style="left:54px;top:275px;width:44px;height:42px;background:linear-gradient(#f4f4f4,#c9c9cb);border:1px solid #ddd"></div>
  <div class="placeholder" role="img" aria-label="Vehicle GPS tracker unit photo" style="left:116px;top:275px;width:44px;height:42px;background:linear-gradient(#eee,#bdbdbf);border:1px solid #ddd"></div>
  <div class="placeholder" role="img" aria-label="Personal key tag tracker photo" style="left:178px;top:275px;width:44px;height:42px;background:linear-gradient(#eef3fa,#8fb1d8);border:1px solid #ddd"></div>
  <svg class="swoosh" style="height:60px" viewBox="0 0 285 60" preserveAspectRatio="none" aria-hidden="true">
    <path d="M0 30 Q140 0 285 25 L285 60 L0 60Z" fill="#e2e2e3"/>
    <path d="M0 45 Q150 20 285 40 L285 60 L0 60Z" fill="#d2d2d4"/>
  </svg>
</section>

<!-- Vehicle Live Tracking -->
<section class="page row-top col-4">
  <h2 class="heading" style="left:40px;top:40px">Vehicle Live Tracking</h2>
  <p class="subhead" style="left:40px;top:62px">Our Vehicle Live Tracking offers the following features:</p>
  <div class="bar" style="left:35px;top:86px;width:80px">Live Tracking</div>
  <div class="bar" style="left:150px;top:86px;width:94px">History</div>
  <p class="body-text" style="left:44px;top:100px;width:72px;font-size:4.5px">Works from GPS location and communicates by GPRS network, you can log onto our website to view the exact location of your vehicle on online maps and the direction of the travelling vehicle.</p>
  <p class="body-text" style="left:154px;top:100px;width:88px;font-size:4.5px">Our web site stores history of the vehicle, enabling you to view the actual route of the vehicle has taken in the past, displayed on maps.</p>
  <div class="bar" style="left:35px;top:164px;width:80px">Report</div>
  <div class="bar" style="left:150px;top:164px;width:94px">Alarms</div>
  <p class="body-text" style="left:44px;top:178px;width:72px;font-size:4.5px">Our website provides you with useful information on your vehicle:</p>
  <p class="body-text" style="left:154px;top:178px;width:88px;font-size:4.5px">All our units have the ability to set the following alarms:</p>
  <div class="feature-box" style="left:35px;top:210px;width:38px;height:40px"><b>STOP REPORT</b>The location your vehicle is stopping and for how long.</div>
  <div class="feature-box" style="left:77px;top:210px;width:38px;height:40px"><b>DISTANCE REPORT</b>The location your vehicle is stopping and for how long.</div>
  <div class="feature-box" style="left:35px;top:258px;width:38px;height:40px"><b>SPEED REPORT</b>The speed your vehicle is travelling.</div>
  <div class="feature-box" style="left:77px;top:258px;width:38px;height:40px"><b>SOS ALARM</b>The time and location of SOS alarm activation.</div>
  <div class="feature-box" style="left:33px;top:310px;width:82px;height:18px;background:var(--bar-grey);color:#fff"><span style="color:#fff">Report format – All reports can be exported to PDF or spreadsheet format.</span></div>
  <div class="feature-box" style="left:150px;top:210px;width:94px;height:36px"><b>GEO-FENCE</b>A geo-fence (perimeter) can be set for your vehicle. An alarm will be activated when the vehicle travels outside of the geo-fence.</div>
  <div class="feature-box" style="left:150px;top:258px;width:94px;height:36px"><b>SOS ALARM</b>Each vehicle is fitted with a push button SOS alarm located under the steering column or near the ignition key.</div>
  <div class="feature-box" style="left:150px;top:306px;width:94px;height:28px"><b>LOW POWER ALARM</b>The alarm will be set at low power to the tracking unit. All alarms can be handled as an event.</div>
  <svg class="swoosh" style="height:60px" viewBox="0 0 285 60" preserveAspectRatio="none" aria-hidden="true">
    <path d="M0 30 Q140 0 285 25 L285 60 L0 60Z" fill="#e2e2e3"/>
    <path d="M0 45 Q150 20 285 40 L285 60 L0 60Z" fill="#d2d2d4"/>
  </svg>
</section>

<!-- Security features -->
<section class="page row-bottom col-1">
  <p class="subhead" style="left:38px;top:40px;width:210px;font-size:7.5px;line-height:1.35">Our Vehicle Live Tracking Service offers the following security features:</p>
  <div class="bar" style="left:44px;top:75px;width:92px">SOS Button</div>
  <div class="bar" style="left:158px;top:75px;width:92px">Disable Engine</div>
  <p class="body-text" style="left:46px;top:108px;width:86px;font-size:4.6px">It has three programmable call buttons, SOS, call 1 and call 2 which can be programmed to a security officer or family / friends. When the SOS button is pressed, the personal tracker will send a SMS to the pre-programmed number on the SOS button with a distress call. It will also give the Latitude &amp; Longitude of your location. An SOS Alarm will also be activated on our website. The SOS Report will provide your exact location on online maps.</p>
  <p class="body-text" style="left:162px;top:91px;width:86px;font-size:4.6px">Vehicle fitted with our GPS tracking units can disable the engine via SMS.</p>
  <div class="bar" style="left:158px;top:136px;width:92px">Live Tracking of Vehicle</div>
  <p class="body-text" style="left:162px;top:152px;width:86px;font-size:4.6px">Your vehicle can be tracked live by yourself and/or your Security Service.</p>
  <div class="placeholder" role="img" aria-label="Illustration of a car tracked on a perspective street map" style="left:0;top:250px;width:285px;height:160px;border-radius:0;background:linear-gradient(180deg,#ffffff 0%,#ececed 40%,#d9d9da 100%)"></div>
</section>

<!-- Benefits -->
<section class="page row-bottom col-2">
  <p class="subhead" style="left:38px;top:46px">Benefits of Vehicle Live Tracking</p>
  <p class="body-text" style="left:38px;top:60px;width:215px">If you are a business owner, you can have more control on your employees and inventory time through our live tracking services. If you are a goods dispatcher, our service offers you an effective and simple solution to help you make your deliveries on time. No matter what industry you serve, tracking your vehicles can help you.</p>
  <p class="body-text" style="left:38px;top:103px">Benefits of our Vehicle Live Tracking:</p>
  <div class="tick-list" style="left:38px;top:140px;width:215px">
    <div class="tick-item"><svg class="tick" viewBox="0 0 11 11"><rect width="11" height="11" rx="2" fill="var(--yellow)"/><path d="M2.5 5.6 4.6 7.6 8.6 3.4" stroke="#fff" stroke-width="1.4" fill="none"/></svg><span>Boost the security of your vehicles and staff members</span></div>
    <div class="tick-item"><svg class="tick" viewBox="0 0 11 11"><rect width="11" height="11" rx="2" fill="var(--yellow)"/><path d="M2.5 5.6 4.6 7.6 8.6 3.4" stroke="#fff" stroke-width="1.4" fill="none"/></svg><span>Boost your business' efficiency and profitability by using our tracking services</span></div>
    <div class="tick-item"><svg class="tick" viewBox="0 0 11 11"><rect width="11" height="11" rx="2" fill="var(--yellow)"/><path d="M2.5 5.6 4.6 7.6 8.6 3.4" stroke="#fff" stroke-width="1.4" fill="none"/></svg><span>Increase the likelihood of vehicle theft recovery</span></div>
    <div class="tick-item"><svg class="tick" viewBox="0 0 11 11"><rect width="11" height="11" rx="2" fill="var(--yellow)"/><path d="M2.5 5.6 4.6 7.6 8.6 3.4" stroke="#fff" stroke-width="1.4" fill="none"/></svg><span>Serve your customers better by making fast deliveries</span></div>
    <div class="tick-item"><svg class="tick" viewBox="0 0 11 11"><rect width="11" height="11" rx="2" fill="var(--yellow)"/><path d="M2.5 5.6 4.6 7.6 8.6 3.4" stroke="#fff" stroke-width="1.4" fill="none"/></svg><span>Track your vehicles, inventory and employees</span></div>
    <div class="tick-item"><svg class="tick" viewBox="0 0 11 11"><rect width="11" height="11" rx="2" fill="var(--yellow)"/><path d="M2.5 5.6 4.6 7.6 8.6 3.4" stroke="#fff" stroke-width="1.4" fill="none"/></svg><span>Manage your business' assets and resources in a more effective manner</span></div>
  </div>
  <div class="placeholder" role="img" aria-label="Faint perspective street map" style="left:0;top:230px;width:288px;height:180px;border-radius:0;background:linear-gradient(180deg,#ffffff 0%,#f0f0f1 50%,#e1e1e2 100%)"></div>
  <p class="subhead" style="left:0;top:274px;width:288px;text-align:center;font-size:7px;line-height:1.4">Please visit our information website for<br>further information:</p>
  <div style="position:absolute;left:88px;top:302px;width:112px;height:14px;border-radius:3px;background:#6e6e70;color:#fff;font-size:5px;line-height:14px;text-align:center">WWW.HARBORBEACONLOCATE.COM</div>
</section>

<!-- Personal Trackers -->
<section class="page row-bottom col-3">
  <h2 class="heading" style="left:33px;top:52px">Personal Trackers</h2>
  <div class="placeholder" role="img" aria-label="Red and black personal tracker device" style="left:206px;top:36px;width:30px;height:40px;border-radius:8px;background:linear-gradient(160deg,#e03030,#8a1212)"></div>
  <p class="subhead" style="left:33px;top:84px">Harbor Beacon Locate offers Personal Trackers.</p>
  <p class="body-text" style="left:33px;top:98px;width:222px">Harbor Beacon Locate's Personal Tracker is a small device that enables you to remotely track, in real time, the position of a loved one or an important asset. Through our website, you can immediately know the position of your beloved one or asset through this device. The tracker uses GPS technology, cellular phone communication and the internet to provide you with its precise location in seconds.</p>
  <p class="body-text" style="left:33px;top:140px;width:222px">The tracker can be used for many purposes – your high value assets such as your boat or car, your children or elderly parents – enabling you to locate them quickly in the event there is cause for concern.</p>
  <p class="body-text" style="left:43px;top:193px">Key features of our Personal Tracker are:</p>
  <div class="tick-list" style="left:44px;top:216px;width:200px;gap:15px 12px">
    <div class="tick-item"><svg class="tick" viewBox="0 0 11 11"><rect width="11" height="11" rx="2" fill="var(--yellow)"/><path d="M2.5 5.6 4.6 7.6 8.6 3.4" stroke="#fff" stroke-width="1.4" fill="none"/></svg><span>It is small in size. It can be linked to keys or hung around your neck.</span></div>
    <div class="tick-item"><svg class="tick" viewBox="0 0 11 11"><rect width="11" height="11" rx="2" fill="var(--yellow)"/><path d="M2.5 5.6 4.6 7.6 8.6 3.4" stroke="#fff" stroke-width="1.4" fill="none"/></svg><span>It last up to 3 days on one charge.</span></div>
    <div class="tick-item"><svg class="tick" viewBox="0 0 11 11"><rect width="11" height="11" rx="2" fill="var(--yellow)"/><path d="M2.5 5.6 4.6 7.6 8.6 3.4" stroke="#fff" stroke-width="1.4" fill="none"/></svg><span>It can be tracked live and record history on the website.</span></div>
    <div class="tick-item"><svg class="tick" viewBox="0 0 11 11"><rect width="11" height="11" rx="2" fill="var(--yellow)"/><path d="M2.5 5.6 4.6 7.6 8.6 3.4" stroke="#fff" stroke-width="1.4" fill="none"/></svg><span>The website will also have geo-fence, SOS alarm, reports and handle alarms.</span></div>
    <div class="tick-item" style="grid-column:1 / span 2"><svg class="tick" viewBox="0 0 11 11"><rect width="11" height="11" rx="2" fill="var(--yellow)"/><path d="M2.5 5.6 4.6 7.6 8.6 3.4" stroke="#fff" stroke-width="1.4" fill="none"/></svg><span>It has three programmable call buttons, SOS, call 1 and call 2 which can be programmed to a security officer or family / friends. When the SOS button is pressed, the personal tracker will send a SMS to the pre-programmed number on the SOS button with a distress call. It will also give the Latitude &amp; Longitude of your location.</span></div>
  </div>
  <svg class="swoosh" style="height:60px" viewBox="0 0 285 60" preserveAspectRatio="none" aria-hidden="true">
    <path d="M0 30 Q140 0 285 25 L285 60 L0 60Z" fill="#e2e2e3"/>
    <path d="M0 45 Q150 20 285 40 L285 60 L0 60Z" fill="#d2d2d4"/>
  </svg>
</section>

<!-- GPS Live Tracking Monitoring -->
<section class="page row-bottom col-4">
  <h2 class="heading" style="left:30px;top:52px">GPS Live Tracking Monitoring</h2>
  <p class="subhead" style="left:30px;top:80px;width:220px;line-height:1.4">Harbor Beacon Locate Offers its two types of GPS monitoring services:</p>
  <div class="bar" style="left:30px;top:118px;width:222px">Self Monitoring</div>
  <p class="body-text" style="left:44px;top:144px;width:200px">Harbor Beacon Locate will provide you with a user name and password, enabling you to log on to your own individual page and monitor the location of your vehicles or personal trackers.</p>
  <div class="bar" style="left:30px;top:194px;width:222px">Self Monitoring &amp; Security Monitoring (only available in Port Moresby)</div>
  <p class="body-text" style="left:44px;top:220px;width:200px">Harbor Beacon Locate has joined forces with Swift Guard Ltd, Port Moresby's most trusted 24 hour emergency Armed Response Units. Swift Guard Ltd is well known for stolen vehicle retrieval.</p>
  <p class="body-text" style="left:44px;top:250px;width:200px">Self Monitoring &amp; Security Monitoring provides the added protection of a 24 hours security. In addition to being able to monitor your own vehicles, your tracking devices will be programmed to send any alerts to Swift Guard's Control Centre, who will immediately respond accordingly.</p>
  <p style="position:absolute;left:60px;top:312px;font-family:'Questrial',sans-serif;font-size:11px;color:#b8161d">Swift Guard Ltd</p>
</section>

</body>
</html>
```